Whitcombe Legal Group Promo Flyers

** I've increased the payment for this job is hopes of getting some more sophisticated design options. See feedback on current designs for guidance. I want this to be sophisticated, elegant, effective design. Please stay away from the brown/blue color palate that has been used in so many of these design options. It's not working. I'd love to see richer, deeper colors with more dimension. **

The Whitcombe Legal Group is trying to market itself as a law firm that is different than other firms. They listen to clients, meet their guidelines, provide excellent communication and will even start work for free to showcase their expertise. I need three separate flyers that will primarily be used as PDFs, but may on occasion be printed.

We're looking for a clean look.

I've attached two sample infographics that are pieces done by another company in the industry. We like that look (sizes of those are different, but the overall look is good).

Target Market(s)

Insurance companies and corporate executives who buy legal services to help them manage their book of litigation. Typical buyer is in 40s to 50s. Fairly racially diverse.

Industry/Entity Type

Communication

Requirements
Must have
• Each document will be a one-page PDF that can be easily emailed to potential clients. Must be one side only for each.

One flyer each for these three files, which are included:
Whitcombe firm by the numbers
Whitcombe firm client advantage program
Whitc firm overview

Must use firm logo. Contact information should pop.

"Topping the list" piece is an inforgraphic that should really focus on bold use of the numbers or text in blue. Mix up the page and make it fun and interesting.

Logo colors are:

Brown: R: 101 G: 50 B:27, HEX: 65321B

Grey: R:129 G: 145 B:144, HEX: 819190
Nice to have
• Firm website is very dull and uninteresting. These pieces need to pop more than past pieces.

http://www.whitcombelegalgroup-example.com/
Should not have
• No stock photos of people in groups (all law firms use those and they are boring and overdone).

```html
<!DOCTYPE html>
<html lang="en">
<head>
<meta charset="utf-8">
<title>The Whitcombe Legal Group – Topping the Lists</title>
<link rel="stylesheet" href="https://fonts.googleapis.com/css2?family=Crimson+Pro:wght@400;600&family=Encode+Sans+Condensed:wght@300;600&family=Oswald:wght@500&family=Open+Sans:wght@400;600&family=Montserrat:wght@700;800&display=swap">
<style>
  :root {
    --backdrop: #e4e7e9;
    --paper: #ffffff;
    --brown: #65321b;
    --logo-grey: #819190;
    --band-green: #5b7068;
    --band-green-dark: #4e625b;
    --accent-red: #a3241a;
    --headline-blush: #f2d9cc;
    --heading-brown: #6a2a1b;
    --body-grey: #555a5c;
    --ink: #1b1b1b;
    --dot-green: #4f6a62;
    --light-grey: #d6d8d8;
  }
  * { box-sizing: border-box; margin: 0; padding: 0; }
  html, body { width: 1200px; height: 1126px; overflow: hidden; background: var(--backdrop); }
  .flyer {
    position: absolute; left: 198px; top: 42px;
    width: 804px; height: 1042px; overflow: hidden;
    background: var(--paper);
    font-family: "Open Sans", sans-serif;
  }
  .abs { position: absolute; }

  /* firm name */
  .firm-name { left: 36px; top: 34px; font-family: "Crimson Pro", serif; font-weight: 400; font-size: 30px; line-height: 32px; color: var(--brown); }
  .firm-name span { display: block; }

  /* header band */
  .header-band { left: 0; top: 138px; width: 804px; height: 162px; }
  .headline { left: 38px; top: 156px; font-family: "Encode Sans Condensed", sans-serif; font-weight: 300; font-size: 31px; color: var(--headline-blush); }
  .intro { left: 38px; top: 198px; font-family: "Encode Sans Condensed", sans-serif; font-weight: 600; font-size: 17px; line-height: 25px; color: #fff; }
  .web { left: 38px; top: 271px; font-family: "Crimson Pro", serif; font-weight: 600; font-size: 14px; color: #fff; }
  .contact { left: 326px; top: 269px; color: #fff; font-size: 11px; }
  .contact .phone { font-family: "Crimson Pro", serif; font-weight: 600; font-size: 17px; margin-right: 6px; }
  .contact b { font-weight: 600; }
  .under-band { left: 0; top: 298px; width: 804px; height: 80px; background: linear-gradient(#e9eaea, #fff); }

  /* infographic column */
  .stat-bar { left: 37px; top: 332px; width: 226px; height: 35px; background: var(--light-grey); }
  .stat-bar-key { left: 37px; top: 332px; width: 15px; height: 35px; background: var(--band-green); }
  .stat-one { left: 38px; top: 333px; font-family: "Montserrat", sans-serif; font-weight: 800; font-size: 22px; color: #fff; }
  .stat-text { left: 54px; top: 338px; font-family: "Montserrat", sans-serif; font-weight: 800; font-size: 18px; color: var(--ink); }
  .caption { font-family: "Encode Sans Condensed", sans-serif; font-weight: 600; font-size: 12px; line-height: 14px; color: var(--ink); }
  .caption-1 { left: 60px; top: 374px; }
  .tri { width: 0; height: 0; border-left: 5px solid transparent; border-right: 5px solid transparent; border-bottom: 8px solid var(--ink); }
  .tri-1 { left: 44px; top: 377px; }

  .firms-graphic { left: 0; top: 400px; }
  .firms-one { left: 31px; top: 456px; font-family: "Montserrat", sans-serif; font-weight: 800; font-size: 24px; color: #fff; }
  .firms-of { left: 46px; top: 462px; font-family: "Montserrat", sans-serif; font-weight: 800; font-size: 14px; color: #fff; }
  .firms-title { left: 76px; top: 460px; font-family: "Montserrat", sans-serif; font-weight: 800; font-size: 18px; color: var(--ink); }
  .firms-caption { left: 78px; top: 484px; }

  .mag-title { left: 43px; top: 568px; font-family: "Crimson Pro", serif; font-size: 22px; color: #8a8f90; }
  .mag-title small { font-family: "Encode Sans Condensed", sans-serif; font-weight: 600; font-size: 12px; color: var(--ink); }
  .mag-chosen { left: 43px; top: 592px; font-family: "Montserrat", sans-serif; font-weight: 800; font-size: 16px; color: var(--ink); }
  .years { left: 0; top: 617px; }
  .year-label { font-family: "Montserrat", sans-serif; font-weight: 700; font-size: 14px; fill: #fff; text-anchor: middle; }

  .timeline { left: 0; top: 690px; }
  .years-big { right: 528px; top: 724px; font-family: "Montserrat", sans-serif; font-weight: 800; font-size: 22px; color: var(--ink); text-align: right; }
  .years-caption { right: 528px; top: 750px; text-align: right; }

  /* accolades list */
  .accolades { left: 326px; top: 330px; width: 440px; list-style: none; }
  .accolade { margin-bottom: 11px; }
  .accolade h3 { font-family: "Oswald", sans-serif; font-weight: 500; font-size: 15px; letter-spacing: .2px; color: var(--heading-brown); line-height: 20px; }
  .accolade p { font-size: 11px; line-height: 15.5px; color: var(--body-grey); }

  .scene-photo { left: 0; top: 720px; width: 804px; height: 322px;
    background: linear-gradient(to bottom, rgba(255,255,255,0) 0%, rgba(200,202,203,.7) 22%, #9c9fa0 55%, #5d6061 100%); }
  .accolades, .years-big, .years-caption { z-index: 1; }
</style>
</head>
<body>
<main class="flyer">
  <div class="abs firm-name">
    <span>The</span>
    <span>Whitcombe</span>
    <span>Legal Group</span>
  </div>

  <svg class="abs header-band" width="804" height="162" viewBox="0 0 804 162" aria-hidden="true">
    <defs>
      <linearGradient id="redBar" x1="0" y1="0" x2="0" y2="1">
        <stop offset="0" stop-color="#b32a1e"/>
        <stop offset="1" stop-color="#7d1a12"/>
      </linearGradient>
    </defs>
    <rect x="0" y="0" width="804" height="146" fill="var(--band-green)"/>
    <polygon points="0,126 628,126 650,146 804,146 804,160 0,160" fill="url(#redBar)"/>
    <polygon points="628,126 650,146 804,146 804,140 652,140 632,126" fill="var(--band-green-dark)"/>
  </svg>
  <h1 class="abs headline">Topping the Lists in Knowledge, Service and Strategy</h1>
  <p class="abs intro">What differentiates The Whitcombe Legal Group, LLC from other firms is our company philosophy.<br>We realize that in order to be successful, our work must be driven by our passion as well as our talent.</p>
  <div class="abs web">www.whitcombelegalgroup-example.com</div>
  <div class="abs contact"><span class="phone">555-010-4821</span> Contact <b>Graham Ellery</b> or <b>Neil Harmon</b></div>
  <div class="abs under-band"></div>

  <div class="abs scene-photo" role="img" aria-label="Photograph of a business meeting in silhouette before a glass wall and city skyline"></div>

  <div class="abs stat-bar"></div>
  <div class="abs stat-bar-key"></div>
  <div class="abs stat-one">1</div>
  <div class="abs stat-text">of 14...</div>
  <div class="abs tri tri-1"></div>
  <p class="abs caption caption-1">Illinois Supreme Court Justices picked<br>their law clerks from our firm.</p>

  <svg class="abs firms-graphic" width="220" height="170" viewBox="0 0 220 170" aria-hidden="true">
    <circle cx="116" cy="82" r="68" fill="#fff" stroke="var(--light-grey)" stroke-width="1.5"/>
    <circle cx="172" cy="74" r="23" fill="var(--light-grey)"/>
    <circle cx="48" cy="74" r="24" fill="var(--dot-green)"/>
    <polygon points="38,92 46,92 42,85" fill="#fff"/>
  </svg>
  <div class="abs firms-one">1</div>
  <div class="abs firms-of">of</div>
  <div class="abs firms-title">2 firms...</div>
  <p class="abs caption firms-caption">selected by one<br>of the industry's<br>largest insurance<br>companies</p>

  <div class="abs mag-title">Top Counsel <small>Magazine</small></div>
  <div class="abs mag-chosen">chosen in...</div>
  <svg class="abs years" width="240" height="50" viewBox="0 0 240 50" aria-hidden="true">
    <circle cx="-6" cy="24" r="23" fill="var(--light-grey)"/>
    <text class="year-label" x="-6" y="29">2009</text>
    <circle cx="48" cy="24" r="23" fill="var(--dot-green)"/>
    <polygon points="43,5 53,5 48,12" fill="#fff"/>
    <text class="year-label" x="48" y="29">2010</text>
    <circle cx="101" cy="24" r="23" fill="var(--light-grey)"/>
    <text class="year-label" x="101" y="29">2011</text>
    <circle cx="154" cy="24" r="23" fill="var(--light-grey)"/>
    <text class="year-label" x="154" y="29">2012</text>
    <circle cx="207" cy="24" r="23" fill="var(--dot-green)"/>
    <polygon points="202,5 212,5 207,12" fill="#fff"/>
    <text class="year-label" x="207" y="29">2013</text>
  </svg>

  <svg class="abs timeline" width="300" height="40" viewBox="0 0 300 40" aria-hidden="true">
    <text x="18" y="11" font-family="Open Sans, sans-serif" font-size="8" fill="#333">180</text>
    <text x="147" y="11" font-family="Open Sans, sans-serif" font-size="8" fill="#333">190</text>
    <line x1="3" y1="23" x2="266" y2="23" stroke="var(--dot-green)" stroke-width="4" stroke-linecap="round" stroke-dasharray="0 9.4"/>
    <polygon points="265,35 275,35 270,27" fill="var(--ink)"/>
  </svg>
  <div class="abs years-big">200 years...</div>
  <p class="abs caption years-caption">of combined business and litigation experience<br>among our top commercial business lawyers</p>

  <ul class="abs accolades">
    <li class="accolade"><h3>ONE CHOSEN...</h3><p>when the Chief Justice of the Illinois Court of Claims picked his law clerk.</p></li>
    <li class="accolade"><h3>HELPED SAVE THE COMPANY...</h3><p>when manufacturing and real estate development companies were facing litigation from one of the largest environmental contamination sites in Illinois.</p></li>
    <li class="accolade"><h3>WROTE THE BOOK...</h3><p>for the State Bar Council, “Handling the Business Emergency: Temporary Restraining Orders and Preliminary Injunctions”.</p></li>
    <li class="accolade"><h3>ON THE TEAM...</h3><p>that helped the largest CEO member organization expand into the Chicago market.</p></li>
    <li class="accolade"><h3>FIRST TO DEVELOP...</h3><p>market and use litigation management software to monitor and report performance.</p></li>
    <li class="accolade"><h3>ALWAYS LEARNING AND GROWING...</h3><p>part of the graduating class of the ALP’s Litigation Management Institute, hosted at Harborview Law School.</p></li>
    <li class="accolade"><h3>FIRST TO THE FUTURE....</h3><p>on the beta development team for the use of technology &amp; information management on one of the first sick building cases in the country coordinating process and claims with the carrier, the insured and the claimants.</p></li>
    <li class="accolade"><h3>BUILDING THE COMPANY,...</h3><p>bet the company, save the company litigation team members on multiple occasions.</p></li>
  </ul>
</main>
</body>
</html>
```